依頼詳細
上記内容でお願い致します。必ず1つは選定致します。
記載項目
表面:会社名/役職/住所/電話番号/メールアドレス/LINEID
裏面:事業内容
希望イメージ
シンプル 複雑
単色 カラフル
暗い 明るい
日常 高級
遊び心 厳粛
未来的 伝統的
女性的 男性的
希望する色
赤系、青系、黄・オレンジ系
納品ファイル
• イラストレーター形式 (.ai)
補足説明

スタイリッシュでハイセンスな所が気に入りました!

ご協力いただきありがとうございました。また機会がございましたらよろしくお願い致します。

```html
<!DOCTYPE html>
<html lang="ja">
<head>
<meta charset="UTF-8">
<title>NOVARK 名刺デザイン</title>
<link rel="stylesheet" href="https://fonts.googleapis.com/css2?family=Noto+Sans+JP:wght@400;500;700&display=swap">
<style>
  :root {
    --page-bg: #dcdcdc;
    --label: #555555;
    --card-white: #ffffff;
    --ink: #2b2b2b;
    --ink-soft: #555555;
    --rule: #c9c9c9;
    --gold-light: #efe6cf;
    --gold: #c9ad74;
    --gold-deep: #a9874a;
    --accent: #d9592a;
    --accent-back: #d95a2b;
    --on-accent: #ffffff;
  }
  * { margin: 0; padding: 0; box-sizing: border-box; }
  html, body { width: 805px; height: 1200px; overflow: hidden; }
  body {
    background: var(--page-bg);
    font-family: "Noto Sans JP", sans-serif;
    color: var(--ink);
    position: relative;
  }
  .side-label {
    position: absolute;
    left: 59px;
    font-size: 21px;
    color: var(--label);
    letter-spacing: 0.5px;
  }
  .side-label--front { top: 66px; }
  .side-label--back { top: 614px; }

  .card {
    position: absolute;
    left: 59px;
    width: 692px;
    height: 390px;
    overflow: hidden;
    box-shadow: 0 2px 6px rgba(0,0,0,0.18);
  }
  .card--front { top: 120px; background: var(--card-white); }
  .card--back { top: 670px; background: var(--accent-back); color: var(--on-accent); }

  /* Front */
  .front-swoosh { position: absolute; left: 0; bottom: 0; width: 692px; height: 200px; }
  .brand-mark {
    position: absolute;
    left: 52px;
    top: 108px;
    width: 190px;
    text-align: center;
  }
  .brand-mark__square {
    display: block;
    width: 34px; height: 34px;
    margin: 0 auto 10px;
    background: var(--accent);
  }
  .brand-mark__name {
    font-size: 34px;
    font-weight: 700;
    letter-spacing: 4px;
    color: var(--ink);
  }
  .profile { position: absolute; left: 318px; top: 62px; width: 340px; }
  .profile__title { font-size: 15px; color: var(--ink-soft); }
  .profile__name-row {
    display: flex; align-items: baseline; gap: 18px;
    margin-top: 8px; padding-bottom: 10px;
    border-bottom: 2px solid var(--rule);
  }
  .profile__name { font-size: 30px; font-weight: 500; letter-spacing: 6px; }
  .profile__roman { font-size: 13px; color: var(--ink-soft); }
  .company { margin-top: 26px; font-size: 22px; font-weight: 500; letter-spacing: 1px; }
  .contact-list { list-style: none; margin-top: 6px; }
  .contact-list li {
    display: flex; align-items: center; gap: 8px;
    font-size: 14.5px; line-height: 1.2; margin-top: 4px;
  }
  .contact-list .address-line { padding-left: 28px; margin-top: 0; }
  .icon {
    width: 20px; height: 20px; flex: none;
    background: var(--accent); border-radius: 2px;
    display: flex; align-items: center; justify-content: center;
  }
  .icon svg { width: 14px; height: 14px; }

  /* Back */
  .back-brand {
    position: absolute; left: 0; right: 0; top: 72px;
    text-align: center;
  }
  .back-brand__square {
    display: block; width: 40px; height: 40px;
    margin: 0 auto 12px; background: var(--on-accent);
  }
  .back-brand__name { font-size: 40px; font-weight: 700; letter-spacing: 5px; }
  .back-rule {
    position: absolute; left: 190px; width: 420px; top: 212px;
    border-top: 1.5px solid rgba(255,255,255,0.85);
  }
  .business-list {
    position: absolute; left: 140px; top: 228px;
    list-style: none; font-size: 15px;
  }
  .business-list li { display: flex; align-items: center; gap: 8px; margin-top: 10px; }
  .business-list li::before {
    content: ""; width: 8px; height: 8px; border-radius: 50%;
    background: var(--on-accent); flex: none;
  }
</style>
</head>
<body>
  <p class="side-label side-label--front">Front</p>
  <section class="card card--front">
    <svg class="front-swoosh" viewBox="0 0 692 200" preserveAspectRatio="none" aria-hidden="true">
      <defs>
        <linearGradient id="gold-band" x1="0" y1="0" x2="1" y2="0">
          <stop offset="0" stop-color="var(--gold-deep)"/>
          <stop offset="0.5" stop-color="var(--gold)"/>
          <stop offset="1" stop-color="var(--gold-light)"/>
        </linearGradient>
      </defs>
      <path d="M0 120 C180 60 420 40 692 90 L692 200 L0 200 Z" fill="var(--gold-light)"/>
      <path d="M0 150 C200 80 430 70 692 120 L692 200 L0 200 Z" fill="url(#gold-band)"/>
      <path d="M0 172 C220 110 450 110 692 150 L692 200 L0 200 Z" fill="#ffffff"/>
    </svg>

    <div class="brand-mark">
      <span class="brand-mark__square"></span>
      <span class="brand-mark__name">NOVARK</span>
    </div>

    <div class="profile">
      <p class="profile__title">代表取締役</p>
      <div class="profile__name-row">
        <span class="profile__name">佐藤 健一</span>
        <span class="profile__roman">Kenichi Sato</span>
      </div>
      <p class="company">NOVARK</p>
      <ul class="contact-list">
        <li><span class="icon"><svg viewBox="0 0 14 14"><path d="M7 2 L1 7 H3 V12 H11 V7 H13 Z" fill="#fff"/></svg></span>〒108-0023</li>
        <li class="address-line">東京都港区芝浦 5-6-78</li>
        <li><span class="icon"><svg viewBox="0 0 14 14"><path d="M3 1 L5.5 1 L6.5 4 L5 5.2 C5.8 7 7 8.2 8.8 9 L10 7.5 L13 8.5 L13 11 C13 12 12 13 11 13 C6 12.5 1.5 8 1 3 C1 2 2 1 3 1 Z" fill="#fff"/></svg></span>03-0000-0000</li>
        <li><span class="icon"><svg viewBox="0 0 14 14"><rect x="1.5" y="3" width="11" height="8" fill="none" stroke="#fff" stroke-width="1.4"/><path d="M1.5 3 L7 8 L12.5 3" fill="none" stroke="#fff" stroke-width="1.4"/></svg></span>info@example.com</li>
        <li><span class="icon"><svg viewBox="0 0 14 14"><ellipse cx="7" cy="6.5" rx="5.5" ry="4.3" fill="#fff"/><path d="M5 10 L4.5 13 L8 10.5 Z" fill="#fff"/></svg></span>lineid</li>
      </ul>
    </div>
  </section>

  <p class="side-label side-label--back">Back</p>
  <section class="card card--back">
    <div class="back-brand">
      <span class="back-brand__square"></span>
      <span class="back-brand__name">NOVARK</span>
    </div>
    <div class="back-rule"></div>
    <ul class="business-list">
      <li>通信回線・通信系サービスの営業(訪問・テレマーケティング)</li>
      <li>各代理店が獲得してきた案件の取次代行、バックヤード業務</li>
      <li>時代のニーズに適合する商品の提案・販売</li>
    </ul>
  </section>
</body>
</html>
```